New Modern floristry business design

Hi, we are a new business based in Sydney called "copper fern floristry"

With so many floristry's we need a good design that will set a great first impression.

A few descriptive words on how we envision copper fern floristry:

-dynamic design
-minimal colour (colour can be used to enhance the design)
-black white grey (can include gold,silver,metallic shadowing)
Strong "COPPER FERN" with a classy "FLORISTRY"
Bold with a touch of feminine

Copper Fern Floristry,
Delia Varnet,
Copperfernfloristry@mailbay.com.au

```html
<!DOCTYPE html>
<html lang="en">
<head>
<meta charset="utf-8">
<title>Copper Fern Floristry – Business Cards</title>
<link rel="stylesheet" href="https://fonts.googleapis.com/css2?family=Tinos:wght@400;700&display=swap">
<style>
  :root {
    --stage: #8a8a8a;
    --card: #1b1b1b;
    --card-pattern: #222222;
    --silver: #d6d6d6;
    --silver-dim: #8e8e8e;
    --ink-light: #ededed;
  }
  * { box-sizing: border-box; margin: 0; padding: 0; }
  html, body { width: 1200px; height: 1000px; overflow: hidden; }
  body {
    background: var(--stage);
    position: relative;
    font-family: "Tinos", "Times New Roman", serif;
  }
  .card {
    position: absolute;
    width: 652px;
    height: 392px;
    border-radius: 14px;
    background: var(--card);
    overflow: hidden;
  }
  .card--front { left: 90px; top: 106px; }
  .card--back { left: 416px; top: 529px; }
  .card__pattern {
    position: absolute;
    inset: 0;
    background: radial-gradient(ellipse at 60% 50%, var(--card-pattern), var(--card));
  }
  .brand {
    position: absolute;
    display: flex;
    align-items: center;
    gap: 20px;
  }
  .brand__mark {
    background: var(--silver);
    flex: none;
  }
  .brand__name {
    font-weight: 700;
    color: var(--silver);
    line-height: 1.15;
    text-transform: uppercase;
    white-space: nowrap;
  }
  .card--front .brand { left: 48px; top: 112px; }
  .card--front .brand__mark { width: 132px; height: 132px; }
  .card--front .brand__name { font-size: 50px; }
  .card--back .brand { left: 128px; top: 36px; }
  .card--back .brand__mark { width: 104px; height: 104px; background: var(--silver-dim); }
  .card--back .brand__name { font-size: 40px; color: var(--silver-dim); }
  .contact {
    position: absolute;
    left: 0;
    right: 0;
    top: 280px;
    text-align: center;
    color: var(--ink-light);
  }
  .contact__name { font-size: 46px; line-height: 1.05; }
  .contact__email { font-size: 26px; line-height: 1.2; }
</style>
</head>
<body>
  <section class="card card--front">
    <div class="card__pattern" role="img" aria-label="Faint dark damask floral pattern across the card"></div>
    <div class="brand">
      <div class="brand__mark"></div>
      <div class="brand__name">Copper Fern<br>Floristry</div>
    </div>
  </section>

  <section class="card card--back">
    <div class="card__pattern" role="img" aria-label="Faint dark damask floral pattern across the card"></div>
    <div class="brand">
      <div class="brand__mark"></div>
      <div class="brand__name">Copper Fern<br>Floristry</div>
    </div>
    <div class="contact">
      <p class="contact__name">Delia Varnet</p>
      <p class="contact__email">Copperfernfloristry@mailbay.com.au</p>
    </div>
  </section>
</body>
</html>
```